Tobin’s letterhead for local government

I require a letterhead for quarterly communications with constituents. The colours I have used in the past are navy & green (together) so I’m happy to use similar colours for this. Please refer to business card as an example.
The letter must make reference to the position I hold which is as per below
“Clr Tobin Kellaway OAM”
And the tag line I have used in the past is “Tobin on Track”. Although I’m not sure if this would be used in a letterhead or not. Happy for this to be provided as an option.
I would like a photo in the letterhead as I believe face recognition is key as an elected member.

Target Market(s)

Political interests

Industry/Entity Type

Government Office

Font styles to use
Sans Serif

Requirements
Must have
• Politically professional. I have been an elected member for 2 years so it is expected that the letterhead conveys that. The colours of the business card is to be used.
Nice to have
• Background of photos to be manipulated or changed to make me stand out, if possible?
Should not have
• Looked like it’s cropped or undertaken by an amateur designer.

```html
<!DOCTYPE html>
<html lang="en">
<head>
<meta charset="utf-8">
<title>Tobin Kellaway – Letterhead</title>
<link rel="stylesheet" href="https://fonts.googleapis.com/css2?family=Arimo:ital,wght@0,400;0,700;1,700&family=Open+Sans:wght@400;600&display=swap">
<style>
  :root {
    --navy: #1f5a94;
    --navy-deep: #1b4f86;
    --green: #0f9447;
    --ink: #3a3a3a;
    --backdrop: #eeeeee;
    --paper: #ffffff;
  }
  * { box-sizing: border-box; margin: 0; padding: 0; }
  html, body { width: 1200px; height: 840px; overflow: hidden; }
  body {
    background: var(--backdrop);
    font-family: "Open Sans", sans-serif;
    position: relative;
  }
  .letterhead {
    position: absolute;
    left: 317px;
    top: 20px;
    width: 566px;
    height: 800px;
    background: var(--paper);
    box-shadow: 0 4px 14px rgba(0,0,0,.18);
    overflow: hidden;
  }
  .top-band { position: absolute; left: 0; top: 0; width: 100%; }
  .top-band__navy { height: 9px; background: var(--navy); }
  .top-band__green { height: 17px; background: var(--green); }

  .councillor-name {
    position: absolute;
    left: 56px;
    top: 50px;
    font-family: "Arimo", sans-serif;
    color: var(--navy);
    line-height: 1.05;
  }
  .councillor-name__first { font-size: 18px; font-weight: 400; display: block; }
  .councillor-name__last { font-size: 19px; font-weight: 700; }
  .councillor-name__honour { font-size: 12px; font-weight: 400; margin-left: 2px; }

  .contact-list {
    position: absolute;
    left: 328px;
    top: 52px;
    list-style: none;
    border-left: 1.5px solid var(--green);
    padding-left: 8px;
    font-size: 7.5px;
    color: var(--navy);
    line-height: 13px;
  }
  .contact-list li { position: relative; }
  .contact-list .contact-icon {
    position: absolute;
    left: -24px;
    top: 3px;
    width: 8px;
    height: 8px;
  }
  .contact-list .contact-icon * { fill: var(--green); }

  .letter-body {
    position: absolute;
    left: 66px;
    top: 168px;
    width: 410px;
    font-size: 9.3px;
    line-height: 15px;
    color: var(--ink);
  }
  .letter-body p { margin-bottom: 15px; }
  .letter-signoff {
    position: absolute;
    left: 96px;
    top: 478px;
    font-size: 9.3px;
    line-height: 15px;
    color: var(--ink);
  }

  .footer-bands { position: absolute; left: 0; bottom: 0; width: 566px; height: 112px; }
  .footer-bands .band-green { fill: var(--green); }
  .footer-bands .band-navy { fill: var(--navy-deep); }

  .portrait {
    position: absolute;
    left: 26px;
    top: 548px;
    width: 150px;
    height: 190px;
    border-radius: 60px 60px 0 0;
    background: linear-gradient(180deg, #c9b6a5 0%, #8b8f96 45%, #3d4250 100%);
  }

  .tagline {
    position: absolute;
    left: 212px;
    top: 718px;
    font-family: "Arimo", sans-serif;
    font-weight: 700;
    font-style: italic;
    font-size: 10px;
    color: #ffffff;
  }
  .social-list {
    position: absolute;
    left: 96px;
    top: 766px;
    width: 440px;
    display: flex;
    justify-content: space-between;
    list-style: none;
    font-size: 8px;
    color: #ffffff;
  }
  .social-list li { display: flex; align-items: center; gap: 4px; }
  .social-dot { width: 8px; height: 8px; border-radius: 50%; background: #ffffff; display: inline-block; }
</style>
</head>
<body>
  <article class="letterhead">
    <div class="top-band">
      <div class="top-band__navy"></div>
      <div class="top-band__green"></div>
    </div>

    <h1 class="councillor-name">
      <span class="councillor-name__first">Clr Tobin</span>
      <span class="councillor-name__last">Kellaway</span><span class="councillor-name__honour">OAM</span>
    </h1>

    <ul class="contact-list">
      <li>
        <svg class="contact-icon" viewBox="0 0 10 10"><path d="M5 0a3.5 3.5 0 0 0-3.5 3.5C1.5 6 5 10 5 10s3.5-4 3.5-6.5A3.5 3.5 0 0 0 5 0zm0 5a1.5 1.5 0 1 1 0-3 1.5 1.5 0 0 1 0 3z"/></svg>
        Address Line 1
      </li>
      <li>Address Line 1</li>
      <li>
        <svg class="contact-icon" viewBox="0 0 10 10"><path d="M2 .5l2 2-1 1.5c.6 1.3 1.7 2.4 3 3l1.5-1 2 2L8 9.5C4 9.5.5 6 .5 2z"/></svg>
        0491 570 118
      </li>
      <li>
        <svg class="contact-icon" viewBox="0 0 10 10"><path d="M0 2h10v6H0zM.8 2.6L5 5.6l4.2-3v-.1H.8z"/></svg>
        tobin@tobinontrack.com
      </li>
      <li>
        <svg class="contact-icon" viewBox="0 0 10 10"><path d="M5 0a5 5 0 1 0 0 10A5 5 0 0 0 5 0zm0 1.5a3.5 3.5 0 1 1 0 7 3.5 3.5 0 0 1 0-7z"/><circle cx="5" cy="5" r="1.6"/></svg>
        www.tobinontrack.com
      </li>
    </ul>

    <section class="letter-body">
      <p>Dear Customer,</p>
      <p>Lorem ipsum dolor sit amet, consectetur adipiscing elit. Aenean ut ipsum eget massa hendrerit vestibulum vel in velit. Donec pretium neque velit.</p>
      <p>Aliquam porta lectus nec mauris ornare venenatis. Vivamus non est turpis, et cursus sem. Mauris vehicula erat in diam auctor at bibendum nisl lacinia.</p>
      <p>Morbi imperdiet neque vehicula nunc convallis gravida. Vestibulum iaculis pretium placerat. Integer consequat, est sit amet facilisis eleifend, nibh nibh varius orci, eget dapibus arcu dui non purus. Pellentesque in magna mauris. Duis enim sapien, dictum vitae condimentum a, pulvinar vel lacus. Mauris et molestie nibh. Vestibulum vitae nulla at metus elementum porta sit amet interdum elit. Nulla sollicitudin neque eu nulla volutpat congue.</p>
      <p>Etiam pellentesque, velit id dapibus fermentum, turpis sapien ornare dui, ac tincidunt ligula odio congue purus. Nunc sed ante dui, in porta lectus. Cras nec sem lorem. In hac habitasse platea dictumst. Maecenas id diam quis dui porta tristique. Sed id egestas felis. Donec ullamcorper mattis posuere. Phasellus fermentum eleifend tortor vel dapibus. Vestibulum ante ipsum.</p>
    </section>

    <p class="letter-signoff">Your Sincerely,<br>Managing Director</p>

    <svg class="footer-bands" viewBox="0 0 566 112" preserveAspectRatio="none">
      <polygon class="band-green" points="0,38 566,2 566,112 0,112"/>
      <polygon class="band-navy" points="0,54 566,20 566,112 0,112"/>
    </svg>

    <div class="portrait" role="img" aria-label="Portrait photo of Clr Tobin Kellaway in a suit and tie"></div>

    <p class="tagline">Tobin on Track</p>

    <ul class="social-list">
      <li><span class="social-dot"></span>@TobinKellaway</li>
      <li><span class="social-dot"></span>@TobinKTrack</li>
      <li><span class="social-dot"></span>@tobin.kellaway</li>
    </ul>
  </article>
</body>
</html>
```